Business cards for start-up accounting firm

I'm looking for a double sided business card ready for upload into Lumo print or similar print providers with no modification required by me.
I'm looking for something simple as i think cards that are too 'busy' actually detract from the message. I have some thoughts but more than happy to see what comes up. The logo i have came out of left field and i love it the moment i saw it!

My thoughts:

Side 1: Just the logo, perhaps on a dark grey or charcoal background to make the logo colours stand out?

Side 2: The call to action from me website 'Looking for a more relaxed, friendly and interactive relationship with your accountant?' with my contact information
Name: Gus Tarrow
Email: gus@ledgerowl.com.au
Website: www.ledgerowl.com.au
Phone: 1300 762 349

The call to action needs to be the first thing they see when they look at side 2. If it helps to know what we do and how we do it there is a draft website at www.ledgerowl.com.au

Like i said, happy to consider anything that comes up :)

Target Market(s)

i'm targeting small business owners who experience a lot of stress around finacial reporting and have had bad experiences with accountants in the past.

Industry/Entity Type

Accounting

Contact Information for Business Card

Contained in the Description

Font styles to use
Serif
Sans Serif
Other font styles liked:
• See logo files attached

Colors
474747

Requirements
Must have
• My logo, slogan and contact information

```html
<!DOCTYPE html>
<html lang="en">
<head>
<meta charset="utf-8">
<title>Ledger Owl – Business Cards</title>
<link rel="stylesheet" href="https://fonts.googleapis.com/css2?family=Ubuntu:wght@400;500;700&display=swap">
<style>
  :root {
    --page: #3b2c2a;
    --charcoal: #272626;
    --panel: #3f3e3f;
    --stripe-light: #e6e6e6;
    --stripe-mid: #a9a9a9;
    --pink: #dc0f63;
    --white: #f4f4f4;
    --muted: #b9b4b8;
    --pink-text: #d2316b;
  }
  * { box-sizing: border-box; margin: 0; padding: 0; }
  html, body { width: 1200px; height: 960px; overflow: hidden; }
  body {
    background: var(--page);
    font-family: "Ubuntu", sans-serif;
    position: relative;
  }
  .card {
    position: absolute;
    width: 608px;
    height: 354px;
    background: var(--charcoal);
    overflow: hidden;
    box-shadow: 6px 8px 14px rgba(0,0,0,0.45);
  }
  .card--front { left: 127px; top: 70px; }
  .card--back { left: 449px; top: 520px; }

  .stripe {
    position: absolute; left: 0; width: 100%; height: 13px;
    background: linear-gradient(to bottom, var(--stripe-mid) 0 3px, var(--stripe-light) 3px 8px, #ffffff 8px 13px);
  }
  .band {
    position: absolute; left: 0; width: 100%; bottom: 0;
    background: var(--pink);
  }
  .card--front .stripe { top: 294px; }
  .card--front .band { top: 307px; }
  .card--back .stripe { top: 291px; }
  .card--back .band { top: 304px; }

  /* Front: brand */
  .brand {
    position: absolute; left: 0; top: 112px; width: 100%;
    display: flex; flex-direction: column; align-items: center;
  }
  .brand__name {
    display: flex; align-items: center; gap: 12px;
    font-weight: 700; font-size: 44px; color: var(--white);
    line-height: 1;
  }
  .brand__dot {
    width: 22px; height: 22px; border-radius: 50%; background: var(--pink);
  }
  .brand__slogan {
    margin-top: 14px;
    font-size: 13px; letter-spacing: 0.3px; color: var(--muted);
  }

  /* Back */
  .person {
    position: absolute; right: 57px; top: 52px; text-align: right;
  }
  .person__name {
    font-weight: 700; font-size: 22px; color: var(--white); letter-spacing: 0.2px;
  }
  .person__role {
    font-size: 14px; color: var(--pink-text); margin-top: 2px;
  }
  .promise {
    position: absolute; left: 39px; top: 106px;
    font-size: 13px; line-height: 18px; color: var(--white); letter-spacing: 0.3px;
  }
  .panel {
    position: absolute; left: 0; top: 210px; width: 100%; height: 81px;
    background: var(--panel);
  }
  .cta {
    position: absolute; left: 39px; top: 20px; width: 340px;
    font-size: 13.5px; line-height: 18px; color: var(--white); letter-spacing: 0.3px;
  }
  .contacts {
    position: absolute; left: 413px; top: 20px; list-style: none;
    font-size: 12px; color: var(--white);
  }
  .contacts li { display: flex; align-items: center; gap: 9px; height: 19.5px; }
  .contacts svg { width: 13px; height: 13px; flex: none; }
</style>
</head>
<body>
  <section class="card card--front" aria-label="Card front">
    <div class="brand">
      <div class="brand__name"><span>Ledger Owl</span><span class="brand__dot"></span></div>
      <div class="brand__slogan">Clear books, calm minds</div>
    </div>
    <div class="stripe"></div>
    <div class="band"></div>
  </section>

  <section class="card card--back" aria-label="Card back">
    <div class="person">
      <div class="person__name">GUS TARROW</div>
      <div class="person__role">Accountant</div>
    </div>
    <p class="promise">We have a special knack for<br>keeping your finances on track.</p>
    <div class="panel">
      <p class="cta">Looking for a more relaxed,friendly and interactive relationship with your accountant?</p>
      <ul class="contacts">
        <li>
          <svg viewBox="0 0 16 16" fill="none" stroke="#d2316b" stroke-width="1.4"><rect x="1.5" y="3.5" width="13" height="9"/><path d="M1.5 3.5 8 9l6.5-5.5"/></svg>
          gus@ledgerowl.com.au
        </li>
        <li>
          <svg viewBox="0 0 16 16" fill="#dc0f63"><path d="M5 1.5h3v3.5H6.5v6H8v3.5H5c-1 0-1.5-.6-1.5-1.5V3c0-.9.5-1.5 1.5-1.5z"/></svg>
          1300 762 349
        </li>
        <li>
          <svg viewBox="0 0 16 16" fill="none" stroke="#d2316b" stroke-width="1.3"><circle cx="8" cy="8" r="6.5"/><ellipse cx="8" cy="8" rx="3" ry="6.5"/><path d="M1.5 8h13"/></svg>
          www.ledgerowl.com.au
        </li>
      </ul>
    </div>
    <div class="stripe"></div>
    <div class="band"></div>
  </section>
</body>
</html>
```